Bright Meadow Co - labels

I have my logo now so its time to proceed with the labels.
The product is organic juices and smoothies. They will be served in Mason jar's and sold as a premium hand made product into the CBD and outlets around Perth such as yoga studios gyms, cafe's etc. Cleanses to individuals etc.
I have attached the logo and a mock of what I would like to see.
I think the logo and the raw organic, handmade look will work with the Chalkboard design and maybe some bunting to brighten the design.
There is currently approx. 10 Juices and Smoothies to the range so I will need to settle on the design and then have you create a label for each one, once settled on the design.
If you have any questions please let me know.

Text on label:
Raw, Organic, Hand Made, Gluten-Free, Dairy-Free

Juice
Morning Vital Sip
Kale, Apple, Celery, Dandelion, Lemon & Ginger

This product is FRESH. Shake before you enjoy!!!

Label size. highest point for height 70 - 75mm. Length 200mm
I also have more wording and nutritional guide for Australian Standards. I will update soon.
Thank you

    Happy Friday Designers!!!

Well I have just increased the budget to $300. I hope this helps to get some designs coming through. If you need anything else from me please send a message.

I look forward to receiving your designs soon and thank you for working with me on my business. this is such an exciting time for me and you guys are making my dream a reality so thank you for your time.

Regards,

Tamsin

Reason: I have not received many designs so extending for a few more days.

Cafe

• Wording - Hand Made
Raw, Organic, Gluten-Free, Dairy-Free
• A chalk board with Juice or Smoothie - Name and ingredients
Bunting I think will work well with the design of logo and chalk board plus bring some colour.

```html
<!DOCTYPE html>
<html lang="en">
<head>
<meta charset="utf-8">
<title>Bright Meadow Co – Juice Label</title>
<link href="https://fonts.googleapis.com/css2?family=Delius&family=Sofia&family=Arimo&display=swap" rel="stylesheet">
<style>
  :root {
    --cream: #feeed2;
    --slate: #4a5056;
    --slate-dark: #3a3f44;
    --label-brown: #bf7410;
    --ring-brown: #d4913a;
    --logo-lime: #d4ec0e;
    --logo-olive: #7f8f1c;
    --check-light: #e4f9c4;
    --check-mid: #b9f05a;
    --check-strong: #8ed31a;
    --juice-green: #6fbd14;
    --stamp-peach: #fbd9b0;
    --stamp-edge: #e8b87a;
    --title-green: #7a9a10;
    --ingredient-grey: #8a8a8a;
    --white: #ffffff;
    --ink: #111111;
  }
  html, body {
    margin: 0;
    width: 1200px;
    height: 900px;
    overflow: hidden;
    background: var(--cream);
  }
  .canvas {
    position: relative;
    width: 1200px;
    height: 900px;
  }
  .base-band {
    position: absolute;
    left: 0;
    top: 812px;
    width: 1200px;
    height: 88px;
    background: linear-gradient(180deg, var(--slate) 0%, var(--slate-dark) 100%);
  }
  .label {
    position: absolute;
    left: 0;
    top: 0;
    filter: drop-shadow(8px 12px 10px rgba(90, 60, 20, 0.35));
  }
  .brand-name { font-family: "Delius", sans-serif; font-size: 20px; fill: var(--logo-olive); }
  .claims { font-family: "Delius", sans-serif; font-size: 19px; fill: var(--white); }
  .product-title { font-family: "Sofia", cursive; font-size: 34px; fill: var(--title-green); }
  .ingredients { font-family: "Sofia", cursive; font-size: 22px; fill: var(--ingredient-grey); }
  .juice-word { font-family: "Sofia", cursive; font-size: 30px; fill: var(--white); }
  .fine-print { font-family: "Arimo", Arial, sans-serif; font-size: 11.5px; fill: var(--ink); }
</style>
</head>
<body>
<div class="canvas">
  <svg class="label" width="1200" height="900" viewBox="0 0 1200 900" xmlns="http://www.w3.org/2000/svg">
    <defs>
      <linearGradient id="check-fill" x1="0" y1="0" x2="0" y2="1">
        <stop offset="0" stop-color="var(--check-light)"/>
        <stop offset="0.5" stop-color="var(--check-mid)"/>
        <stop offset="1" stop-color="var(--check-light)"/>
      </linearGradient>
      <linearGradient id="stamp-fill" x1="0" y1="0" x2="1" y2="1">
        <stop offset="0" stop-color="#fff6ea"/>
        <stop offset="1" stop-color="var(--stamp-peach)"/>
      </linearGradient>
      <pattern id="stitch" width="12" height="12" patternUnits="userSpaceOnUse">
        <line x1="2" y1="10" x2="10" y2="2" stroke="var(--white)" stroke-width="2" stroke-linecap="round"/>
      </pattern>
    </defs>

    <!-- label body -->
    <rect class="label-body" x="375" y="155" width="466" height="550" fill="var(--label-brown)"/>
    <circle cx="608" cy="205" r="112" fill="var(--label-brown)"/>

    <!-- checked cloth field -->
    <rect class="cloth" role="img" aria-label="Green and white gingham cloth pattern"
          x="392" y="170" width="432" height="520" fill="url(#check-fill)"/>
    <rect class="cloth-base" x="392" y="612" width="432" height="78" fill="var(--check-strong)"/>

    <!-- stitching -->
    <rect x="380" y="164" width="12" height="532" fill="url(#stitch)"/>
    <rect x="824" y="164" width="12" height="532" fill="url(#stitch)"/>
    <rect x="380" y="164" width="456" height="12" fill="url(#stitch)"/>
    <rect x="380" y="684" width="456" height="12" fill="url(#stitch)"/>

    <!-- centre banner -->
    <rect class="banner" x="493" y="170" width="225" height="262" fill="var(--label-brown)"/>
    <ellipse class="leaf-motif" role="img" aria-label="Faint leaf illustration"
             cx="660" cy="360" rx="62" ry="44" fill="var(--ring-brown)" opacity="0.45"/>

    <!-- brand seal -->
    <circle cx="608" cy="205" r="96" fill="var(--ring-brown)"/>
    <circle cx="608" cy="205" r="84" fill="var(--logo-lime)"/>
    <circle cx="608" cy="205" r="10" fill="var(--logo-olive)" transform="translate(0 -40)"/>
    <text class="brand-name" x="608" y="200" text-anchor="middle">Bright Meadow</text>
    <text class="brand-name" x="608" y="226" text-anchor="middle">Co</text>

    <!-- claims -->
    <text class="claims" x="612" y="322" text-anchor="middle">Raw,</text>
    <text class="claims" x="612" y="346" text-anchor="middle">Organic</text>
    <text class="claims" x="612" y="370" text-anchor="middle">Gluten-Free</text>
    <text class="claims" x="612" y="394" text-anchor="middle">Dairy-Free</text>

    <!-- stamp panel -->
    <g class="stamp" transform="translate(606 522) rotate(-6)">
      <rect x="-176" y="-98" width="352" height="196" fill="none" stroke="var(--stamp-edge)"
            stroke-width="17" stroke-dasharray="0 16" stroke-linecap="round"/>
      <rect x="-176" y="-98" width="352" height="196" fill="none" stroke="var(--white)"
            stroke-width="14" stroke-dasharray="0 16" stroke-linecap="round"/>
      <rect x="-176" y="-98" width="352" height="196" fill="var(--white)"/>
      <rect x="-158" y="-80" width="316" height="160" fill="url(#stamp-fill)" stroke="var(--stamp-edge)" stroke-width="2"/>
      <text class="product-title" x="0" y="-28" text-anchor="middle">Morning Vital Sip</text>
      <text class="ingredients" x="0" y="22" text-anchor="middle">Kale, Apple, Celery, Dandelion,</text>
      <text class="ingredients" x="0" y="50" text-anchor="middle">Lemon &amp; Ginger</text>
    </g>

    <!-- footer -->
    <text class="fine-print" x="417" y="653">This product is FRESH.</text>
    <text class="fine-print" x="653" y="653">Shake before you enjoy!!!</text>
    <circle class="juice-badge" cx="600" cy="665" r="38" fill="var(--juice-green)"/>
    <text class="juice-word" x="600" y="675" text-anchor="middle">Juice</text>
  </svg>

  <div class="base-band"></div>
</div>
</body>
</html>
```